Flyer-Design für Werbeflyer Teamentwicklung/Coaching als pdf
Zielgruppe
ich berate Personen, Teams und Organisationseinheiten, überwiegend im Profitbereich. (Internationale Konzerne). Mein Beratungsspektrum ist Führung, Prozessverbesserungen, Teamentwicklung
Aufgabenstellung
Der Text ist in Anlehnung an meine HP, Teamentwicklung und Coaching und es sollte eine übersichtliche, infomative 1-2 Seiten entstehen, die ich als erste Werbung/Kontaktaufnahme versenden kann. Die Seiten sollen klar einen Überblick über mein "Schaffen" geben, sollen aber auch schon etwas von meiner Arbeitsweise deutlich machen. (Ich begriefe schnell, formuliere klar und arbeite sehr zielorientiert - allerdings auch schnörkellos!) Diese Seiten sollten überwiegend als Anhang an eine Mail fungieren, im Ausnahmefall aber auch versendet werden.
Das Logo, die Farbe, etc. analog zu meiner HP - ich lass mich da aber auch gern beraten, falls sie andere Ideen haben

```html
<!DOCTYPE html>
<html lang="de">
<head>
<meta charset="utf-8">
<title>Teamentwicklung – Brigitte Moser</title>
<link rel="stylesheet" href="https://fonts.googleapis.com/css2?family=Open+Sans:wght@400;600;700&family=Tinos:wght@700&display=swap">
<style>
  :root {
    --band: #b9cbc5;
    --plum: #74104f;
    --slate: #6a7372;
    --frame: #8f9a98;
    --logo-dark: #9aa8a8;
    --paper: #ffffff;
    --text: #6b7372;
  }
  * { box-sizing: border-box; margin: 0; padding: 0; }
  html, body { width: 1200px; height: 846px; overflow: hidden; background: var(--paper); }
  body { font-family: "Open Sans", Arial, sans-serif; color: var(--text); }

  .flyer { position: relative; width: 1200px; height: 846px; overflow: hidden; background: var(--paper); }

  .hero-photo {
    position: absolute; left: 0; top: 0; width: 351px; height: 846px;
    background: linear-gradient(180deg, #4da6d8 0%, #8fd0ea 22%, #c9e6ea 36%, #b7b0a0 48%, #8c7a64 66%, #6e5c48 100%);
  }

  .accent-block { position: absolute; left: 1043px; top: 0; width: 109px; height: 228px; background: var(--plum); }

  .top-band { position: absolute; left: 0; top: 27px; width: 1200px; height: 115px; background: var(--band); }

  .brand {
    position: absolute; left: 45px; top: 27px; width: 122px; height: 115px;
    background: linear-gradient(90deg, var(--logo-dark) 50%, var(--paper) 50%);
    display: flex; align-items: center; justify-content: center;
  }
  .brand-name { font-size: 19px; font-weight: 600; color: var(--slate); background: var(--paper); padding: 2px 6px; }

  .motto { position: absolute; left: 680px; top: 33px; width: 480px; height: 102px; }
  .motto svg { position: absolute; inset: 0; }
  .motto-text {
    position: absolute; font-family: "Tinos", "Times New Roman", serif; font-weight: 700;
    font-size: 21px; color: var(--paper); line-height: 1;
  }
  .motto-line1 { left: 35px; top: 23px; }
  .motto-line2 { left: 109px; top: 58px; }

  .intro-box {
    position: absolute; left: 48px; top: 168px; width: 674px; height: 199px;
    border: 6px solid var(--frame); background: rgba(255,255,255,0.78);
    padding: 20px 24px 0 26px;
  }
  .intro-title { color: var(--plum); font-size: 32px; font-weight: 400; letter-spacing: 0.3px; line-height: 40px; margin-bottom: 14px; }
  .intro-text { font-size: 18.5px; line-height: 24px; color: var(--text); }

  .page-title { position: absolute; right: 48px; top: 294px; text-align: right; color: var(--slate); font-weight: 600; }
  .page-title h1 { font-size: 35px; line-height: 42px; font-weight: 600; letter-spacing: 0.5px; }
  .page-title .person { font-size: 28px; line-height: 34px; letter-spacing: 0.5px; }
  .page-title .person em { font-style: normal; color: var(--plum); }

  .services { position: absolute; left: 410px; top: 393px; width: 355px; }
  .services h2 { font-size: 18px; font-weight: 600; color: var(--slate); margin-bottom: 22px; }
  .services ul { list-style: none; }
  .services li { position: relative; padding-left: 26px; font-size: 19px; line-height: 22px; margin-bottom: 14px; hyphens: auto; }
  .services li::before { content: ""; position: absolute; left: 0; top: 6px; width: 12px; height: 12px; background: var(--plum); }

  .description { position: absolute; left: 816px; top: 438px; width: 340px; font-size: 19px; line-height: 22px; hyphens: auto; }
</style>
</head>
<body>
<main class="flyer">
  <div class="hero-photo" role="img" aria-label="Foto: hölzerner Steg mit weißem Geländer, der unter blauem Himmel aufs Meer hinausführt"></div>
  <div class="accent-block"></div>
  <div class="top-band"></div>

  <div class="brand"><span class="brand-name">Moser</span></div>

  <blockquote class="motto">
    <svg width="480" height="102" viewBox="0 0 480 102" fill="none" stroke="#fff" stroke-width="4">
      <polyline points="60,2 28,2 28,100 60,100"/>
      <polyline points="416,2 470,2 470,100 454,100"/>
    </svg>
    <svg width="480" height="102" viewBox="0 0 480 102">
      <text x="18" y="34" fill="#fff" font-family="Tinos, serif" font-weight="700" font-size="30">“</text>
      <text x="474" y="92" fill="#fff" font-family="Tinos, serif" font-weight="700" font-size="30">”</text>
    </svg>
    <span class="motto-text motto-line1">Zu erkennen was geschieht,</span>
    <span class="motto-text motto-line2">ist der Beginn der Veränderung.</span>
  </blockquote>

  <section class="intro-box">
    <h2 class="intro-title">TEAMENTWICKLUNG</h2>
    <p class="intro-text">Teams sind lebendige Gebilde, die um erfolgreich zu sein, sich immer wieder neu ausrichten und koordinieren müssen. Das tun sie in aller Regel ohne fremde Hilfe - aber ab und zu ist es hilfreich, Impulse oder Entwicklungsförderung von außen bekommen.</p>
  </section>

  <header class="page-title">
    <h1>TEAMENTWICKLUNG</h1>
    <p class="person">BRIGITTE <em>MOSER</em></p>
  </header>

  <section class="services">
    <h2>DAZU GEHÖREN</h2>
    <ul>
      <li>Eine sorgfältige Analyse der Situation und Festlegung gewünschter Resultate</li>
      <li>Überzeugende und förderliche Methoden, die die Lösungskompetenzen der Menschen im Team unterstützen</li>
      <li>Klare Führung durch den Widerstreit von Teaminteressen zwischen Verändern, Bewahren, Harmonie und Konfliktbearbeitung, klarem Feedback und Eintracht im Team</li>
      <li>Tragfähigkeit der Ergebnisse</li>
    </ul>
  </section>

  <p class="description" lang="la">Is quiant, sequo tempore peligenimus dollest isitiur aut provitat eos magnationsed qui dolore plaborunt as archita doluptatia deri audam essi optatur ratiist abor aut laut eatium faccuptae et aut ut es sequam recest qui nem re es seque parchit apictem quid et volorererro eniasperem inimporem quam, il iscipidit officidi omnis culpa sus secabo. Sed et arum illenis simus sus recerrum des ut aut il magni consent. perem inimporem quam, il iscipidit officidi omnis culpa sus secabo. Sed et arum illenis simus sus recerrum des ut aut il magni consent.</p>
</main>
</body>
</html>
```